Business Card Design Project

Hello! We need a business card design for a new company opening up in Downtown Dallas called Marbrook Cupcakes. We are a cupcake factory and our primary colors are Harbor Teal and Brown. We want to have a design that can be used for multiple positions (Owner/Operations Manager, Assistant Operations Manager, Decorator, Baker, Corporate Sale Rep, Special Events Rep etc) We would like for it to be double sided. Use the following information in your designs:

Renata Vasquill
Assistant Operations Manager
renata@marbrookcupcakes.example
T555.318.9047

Store Hours:
Mon-Thur 10am-9pm
Fri-Sat 10am-10pm
Sun 12pm-7pm

website: www.marbrookcupcakes.example

Address: 2735 Quarry Ln, Dallas TX 75999

The logo is attached.

Industry/Entity Type

Business

Requirements
Must have
• It must be Harbor Teal and Brown.
Nice to have
• Nice for it to be double sided.
Should not have
• No graphics like a cupcake. Just the word logo.

```html
<!DOCTYPE html>
<html lang="en">
<head>
<meta charset="utf-8">
<title>Marbrook Cupcakes – Business Cards</title>
<link rel="stylesheet" href="https://fonts.googleapis.com/css2?family=PT+Sans:wght@400;700&family=Questrial&display=swap">
<style>
  :root {
    --harbor-teal: #66c6cf;
    --teal-text: #5bbfc9;
    --cocoa: #43170c;
    --cocoa-text: #4a1c0e;
    --ink: #2b2b2b;
    --paper: #ffffff;
    --stage: #7a4f30;
    --label: #2a1a10;
  }
  html, body {
    margin: 0;
    padding: 0;
    overflow: hidden;
  }
  body {
    width: 1200px;
    height: 788px;
    background: var(--stage);
    position: relative;
    font-family: "PT Sans", sans-serif;
  }
  .view-label {
    position: absolute;
    width: 525px;
    text-align: center;
    font-size: 22px;
    color: var(--label);
    margin: 0;
    font-weight: 400;
  }
  .card {
    position: absolute;
    width: 525px;
    height: 300px;
    border-radius: 22px;
    overflow: hidden;
  }
  .card--white { background: var(--paper); }
  .card--teal { background: var(--harbor-teal); }
  .card--cocoa { background: var(--cocoa); }
  .wordmark {
    position: absolute;
    left: 0;
    width: 100%;
    text-align: center;
    font-family: "Questrial", sans-serif;
    font-weight: 400;
    line-height: 1;
  }
  .wordmark__name { display: block; font-size: 54px; }
  .wordmark__sub { display: block; font-size: 28px; margin-top: 4px; padding-left: 150px; }
  .wordmark--teal { color: var(--teal-text); }
  .wordmark--white { color: var(--paper); }
  .abs { position: absolute; margin: 0; white-space: nowrap; }
  .person-name { font-size: 17px; font-weight: 700; color: var(--cocoa-text); }
  .person-title { font-size: 13px; color: var(--teal-text); letter-spacing: 0.3px; }
  .contact { font-size: 14px; color: var(--ink); }
  .contact b { font-style: italic; }
  .bands { position: absolute; left: 0; top: 0; }
  .band-text { font-size: 14px; color: var(--paper); }
  .band-text--dark { color: var(--ink); }
  .hours { font-size: 15px; line-height: 20px; text-align: center; left: 0; width: 100%; }
  .hours b { font-weight: 700; }
  .hours--cocoa { color: var(--cocoa-text); }
  .hours--dark { color: var(--ink); font-size: 14px; }
  .site {
    left: 0; width: 100%; text-align: center;
    font-family: "Questrial", sans-serif;
    font-size: 17px; letter-spacing: 2.4px;
  }
  .site--grey { color: #333; }
  .site--white { color: var(--paper); }
  .hours-split { color: var(--paper); font-size: 14px; line-height: 17px; }
  .hours-split b { font-weight: 700; }
  .divider { position: absolute; width: 1px; background: rgba(255,255,255,0.6); }
</style>
</head>
<body>

  <h2 class="view-label" style="left:53px; top:32px;">Front</h2>
  <h2 class="view-label" style="left:622px; top:32px;">Back - 1</h2>
  <h2 class="view-label" style="left:53px; top:403px;">Back - 2</h2>
  <h2 class="view-label" style="left:622px; top:403px;">Back - 3</h2>

  <!-- Front -->
  <section class="card card--white" style="left:53px; top:74px;">
    <div class="wordmark wordmark--teal" style="top:44px; left:-20px;">
      <span class="wordmark__name">Marbrook</span>
      <span class="wordmark__sub">cupcakes</span>
    </div>
    <p class="abs person-name" style="left:22px; top:160px;">Renata Vasquill</p>
    <p class="abs person-title" style="left:22px; top:181px;">Assistant Operations Manager</p>
    <p class="abs contact" style="left:312px; top:157px;"><b>p</b> : 555.318.9047</p>
    <p class="abs contact" style="left:312px; top:182px;">2735 Quarry Ln, Dallas TX 75999</p>
    <svg class="bands" width="525" height="300" viewBox="0 0 525 300" aria-hidden="true">
      <polygon points="0,213 307,213 281,243 0,243" fill="#43170c"/>
      <polygon points="268,266 242,231 525,231 525,266" fill="#66c6cf"/>
    </svg>
    <p class="abs band-text" style="left:22px; top:220px;">renata@marbrookcupcakes.example</p>
    <p class="abs band-text band-text--dark" style="left:312px; top:240px;">www.marbrookcupcakes.example</p>
  </section>

  <!-- Back 1 -->
  <section class="card card--white" style="left:622px; top:74px;">
    <div class="wordmark wordmark--teal" style="top:42px;">
      <span class="wordmark__name">Marbrook</span>
      <span class="wordmark__sub">cupcakes</span>
    </div>
    <p class="abs hours hours--cocoa" style="top:183px;">
      <b>Store Hours</b><br>
      <b>Mon-Thur</b> 10am-9pm | <b>Fri-Sat</b> 10am-10pm<br>
      <b>Sun</b> 12pm-7pm
    </p>
    <p class="abs site site--grey" style="top:266px;">www.marbrookcupcakes.example</p>
  </section>

  <!-- Back 2 -->
  <section class="card card--teal" style="left:53px; top:445px;">
    <div class="wordmark wordmark--white" style="top:36px;">
      <span class="wordmark__name">Marbrook</span>
      <span class="wordmark__sub">cupcakes</span>
    </div>
    <p class="abs hours hours--dark" style="top:203px;">
      <b>Store Hours</b><br>
      <b>Mon-Thur</b> 10am-9pm | <b>Fri-Sat</b> 10am-10pm | <b>Sun</b> 12pm-7pm
    </p>
    <p class="abs site" style="top:268px; color:#1f1f1f;">www.marbrookcupcakes.example</p>
  </section>

  <!-- Back 3 -->
  <section class="card card--cocoa" style="left:622px; top:445px;">
    <div class="wordmark wordmark--teal" style="top:38px;">
      <span class="wordmark__name">Marbrook</span>
      <span class="wordmark__sub">cupcakes</span>
    </div>
    <p class="abs hours-split" style="left:164px; top:173px;"><b>Store Hours</b></p>
    <div class="divider" style="left:263px; top:173px; height:52px;"></div>
    <p class="abs hours-split" style="left:274px; top:174px;">
      <b>Mon-Thur</b> 10am-9pm<br>
      <b>Fri-Sat</b> 10am-10pm<br>
      <b>Sun</b> 12pm-7pm
    </p>
    <p class="abs site site--white" style="top:258px;">www.marbrookcupcakes.example</p>
  </section>

</body>
</html>
```